Web design project for exciting Australian start-up

Background
We are looking for a creative and talented web design artist to work alongside our market leading web developer.
• You will be required to create a modern and clean design theme for our website, incorporating selected rustic colour scheme elements for our exciting Australian start-up to operate within the coffee industry.
reoccurring work to be expected to flow to the successful designer.
Requirements
• c. 5 - 10 page website
• Landing page
• Log in/ out
• 404 template
• Typography is emphasised
• Please use either a) quillnest.com, b) free web fonts, c) plovra fonts
• All design elements in vector format
• Preferably with icons for each header title(i.e. about us, how it works etc) but designer have free reign over how the site looks, so might not be applicable
• All pages to be responsive
• Down to Kelvo resolution

High level visual design brief attached - additional pages to be worked from base design.

Design inspiration
• We would like to use design elements from the following sources:
http://www.plovra.com/vintel/ (Functionality)
Colour scheme refer to logo and complementary style guide

```html
<!DOCTYPE html>
<html lang="en">
<head>
<meta charset="utf-8">
<title>Brewhaven — Dashboard</title>
<link href="https://fonts.googleapis.com/css2?family=Roboto:wght@300;400;500;700&display=swap" rel="stylesheet">
<style>
:root{
  --orange:#f7941d;
  --text:#444;
  --muted:#666;
  --line:#d9d9d9;
  --panel:#f4f4f4;
  --dark:#222;
  --white:#fff;
  --green:#3a8a3e;
}
*{box-sizing:border-box;margin:0;padding:0}
html,body{width:1163px;height:1200px;overflow:hidden;background:var(--white);font-family:'Roboto',sans-serif;font-weight:300;color:var(--text)}
.page{position:relative;width:1163px;height:1200px}
.abs{position:absolute}
/* header */
.brand{left:40px;top:27px;display:flex;align-items:center;gap:10px;font-weight:700;font-size:26px;letter-spacing:2px;color:var(--dark)}
.brand-dot{width:42px;height:42px;border-radius:50%;background:var(--orange)}
.btn{top:39px;height:30px;border:1px solid var(--dark);font-size:13px;display:flex;align-items:center;justify-content:center;color:var(--orange);font-weight:300;background:var(--white)}
.btn.plain{color:var(--dark)}
.header-rule{left:0;top:107px;width:1163px;height:3px;background:var(--orange)}
/* panels */
.panel{border:1px solid var(--line);background:var(--white)}
.panel-head{height:39px;background:var(--panel);border-bottom:1px solid var(--line);font-size:17px;font-weight:400;color:var(--text);padding:10px 0 0 32px}
.photo{left:80px;top:194px;width:153px;height:101px;background:linear-gradient(160deg,#a33 0%,#5a4036 45%,#c9b8a8 100%)}
.nav-box{top:231px;width:30px;height:43px;background:#f2f2f2;display:flex;align-items:center;justify-content:center}
.dots{left:135px;top:309px;display:flex;gap:6px}
.dots span{width:8px;height:8px;border-radius:50%;background:#ccc}
.dots span.on{background:var(--orange)}
.profile{left:61px;top:332px;font-size:17px;line-height:25px;color:var(--muted)}
.profile b{font-weight:400;color:var(--text)}
.acct-item{left:43px;display:flex;gap:14px;font-size:17px;line-height:25px;color:var(--muted)}
.acct-item svg{flex:none;margin-top:5px}
.acct-item strong{font-weight:400;color:var(--text);display:block}
.vdiv{left:298px;top:135px;width:1px;height:591px;background:var(--line)}
/* main */
.section-title{left:318px;font-size:25px;font-weight:300;color:var(--text)}
.section-rule{left:318px;width:586px;height:1px;background:var(--line)}
.filter{font-size:16px;color:var(--muted);display:flex;align-items:center;gap:8px}
.caret-down{width:0;height:0;border-left:5px solid transparent;border-right:5px solid transparent;border-top:6px solid var(--orange)}
.caret-left{width:0;height:0;border-top:5px solid transparent;border-bottom:5px solid transparent;border-right:6px solid var(--orange)}
.caret-right{width:0;height:0;border-top:5px solid transparent;border-bottom:5px solid transparent;border-left:6px solid var(--orange)}
/* right column */
.side-link{left:952px;font-size:17px;color:var(--text);display:flex;align-items:center;gap:11px;font-weight:300}
.deliveries{left:943px;top:330px;width:203px;height:153px;border:1px solid #eee}
.delivery{position:absolute;left:0;width:183px;background:var(--panel);padding:8px 9px;font-size:12px;line-height:19px;color:var(--muted)}
.delivery .time{color:var(--orange);font-size:13px;margin-bottom:4px}
.scrollbar{position:absolute;right:0;top:0;width:18px;height:100%;border-left:1px solid #e3e3e3;background:#fafafa}
.month{left:952px;top:502px;width:179px;display:flex;justify-content:space-between;align-items:center;font-size:18px;color:var(--text)}
.cal{left:950px;top:545px;width:181px;border-collapse:collapse;font-size:12px;font-weight:400;color:var(--dark);text-align:center}
.cal th{font-size:8px;font-weight:400;color:#888;height:18px;border:1px solid #e3e3e3}
.cal td{height:26px;border:1px solid #e3e3e3}
.cal td.today{background:#eee;color:#999}
.download{left:955px;top:709px;display:flex;align-items:center;gap:10px;font-size:15px;color:var(--muted)}
/* footer */
.footer-rule{left:26px;top:751px;width:1120px;height:2px;background:#e6e6e6}
.col-shadow{top:839px;width:2px;height:240px;background:linear-gradient(to bottom,transparent,#ddd 40%,#ddd 60%,transparent)}
.avatar{top:793px;width:103px;height:103px;border-radius:50%}
.col-title{top:914px;width:220px;text-align:center;font-size:23px;font-weight:700;color:var(--dark)}
.links{top:962px;width:136px;list-style:none}
.links li{height:33.5px;border-bottom:1px solid #e6e6e6;display:flex;align-items:center;justify-content:center;gap:8px;font-size:14px;color:var(--muted);font-weight:300}
.social{left:823px;top:952px;width:136px;list-style:none}
.social li{height:37.5px;border-bottom:1px solid #e6e6e6;display:flex;align-items:center;gap:18px;font-size:14px;color:var(--muted)}
.social .icon{width:27px;height:27px;border-radius:50%;background:var(--orange);flex:none}
.bottom-band{left:0;top:1156px;width:1163px;height:44px;background:#f3f3f3;border-top:1px solid #e3e3e3}
.copyright{left:105px;top:1172px;font-size:11px;font-weight:400;color:var(--dark)}
</style>
</head>
<body>
<div class="page">

  <header>
    <div class="abs brand"><span>BREWHAVEN</span><span class="brand-dot"></span></div>
    <div class="abs btn" style="left:809px;width:124px">My Account</div>
    <div class="abs btn" style="left:944px;width:98px">Logged In</div>
    <div class="abs btn plain" style="left:1041px;width:89px">Logout</div>
    <div class="abs header-rule"></div>
  </header>

  <!-- left column -->
  <section class="abs panel" style="left:27px;top:135px;width:259px;height:279px">
    <div class="panel-head">Photos</div>
  </section>
  <div class="abs photo" role="img" aria-label="Photo of a busy café terrace with waiters and guests"></div>
  <div class="abs nav-box" style="left:26px">
    <svg width="12" height="16" viewBox="0 0 12 16"><path d="M10 2 4 8l6 6" stroke="var(--orange)" stroke-width="3" fill="none"/></svg>
  </div>
  <div class="abs nav-box" style="left:256px">
    <svg width="12" height="16" viewBox="0 0 12 16"><path d="M2 2l6 6-6 6" stroke="var(--orange)" stroke-width="3" fill="none"/></svg>
  </div>
  <div class="abs dots"><span></span><span></span><span class="on"></span></div>
  <div class="abs profile">
    <b>Café Marlo</b><br>Melbourne, Australia<br>Member since [Feb, 2014]
  </div>

  <section class="abs panel" style="left:27px;top:448px;width:259px;height:278px">
    <div class="panel-head">My Account</div>
  </section>
  <div class="abs acct-item" style="top:511px">
    <svg width="22" height="16" viewBox="0 0 22 16"><rect x="1" y="1" width="20" height="14" fill="none" stroke="var(--orange)"/><path d="M1 1l10 8 10-8M1 15l7-6M21 15l-7-6" fill="none" stroke="var(--orange)"/></svg>
    <div><strong>Email Address</strong>Verified</div>
  </div>
  <div class="abs acct-item" style="top:578px">
    <svg width="22" height="20" viewBox="0 0 22 20"><path d="M2 6h14v6a6 6 0 0 1-6 6H8a6 6 0 0 1-6-6zM16 8h3v3h-3M8 1v3M11 1v3" fill="none" stroke="var(--orange)"/></svg>
    <div><strong>Café type</strong>(i.e. Café, speciality coffee<br>&nbsp;shop, restaurant)</div>
  </div>
  <div class="abs acct-item" style="top:667px">
    <svg width="22" height="16" viewBox="0 0 22 16"><rect x="1" y="1" width="20" height="14" rx="1" fill="none" stroke="var(--orange)"/><path d="M1 5h20M1 7h20" stroke="var(--orange)"/></svg>
    <div><strong>Payment details</strong>Verified</div>
  </div>

  <div class="abs vdiv"></div>

  <!-- main -->
  <h2 class="abs section-title" style="top:133px">Live Tenders</h2>
  <div class="abs section-rule" style="top:168px"></div>
  <div class="abs filter" style="left:321px;top:178px"><span class="caret-down"></span>Time remaining</div>

  <h2 class="abs section-title" style="top:319px;left:319px">Purchases</h2>
  <div class="abs section-rule" style="top:359px"></div>
  <div class="abs filter" style="left:320px;top:373px"><span class="caret-down"></span>All</div>
  <div class="abs filter" style="left:458px;top:373px">Period (x months)</div>
  <div class="abs filter" style="left:733px;top:373px">Awaiting feedback (x)</div>

  <!-- right column -->
  <div class="abs side-link" style="top:142px;left:966px">Inbox</div>
  <div class="abs side-link" style="top:184px"><span class="caret-down"></span>Messages</div>
  <div class="abs side-link" style="top:222px"><span class="caret-down"></span>Saved searches</div>
  <div class="abs side-link" style="top:262px;width:182px;justify-content:space-between;align-items:flex-start">
    <span class="caret-left" style="margin-top:7px"></span>
    <span style="text-align:center;line-height:25px">Incoming deliveries<br>this week</span>
    <span class="caret-right" style="margin-top:7px"></span>
  </div>

  <div class="abs deliveries">
    <div class="delivery" style="top:0;height:76px">
      <div class="time">8 am – 11 am</div>
      Delivery of order 3220x<br>Order: 20kg Wonder Roast
    </div>
    <div class="delivery" style="top:78px;height:75px">
      <div class="time">11 am – 3 pm</div>
      Delivery of order 3221y<br>Order: Sample testing Verano
    </div>
    <div class="scrollbar">
      <svg width="18" height="153" viewBox="0 0 18 153"><path d="M4 12l5-6 5 6z" fill="var(--orange)"/><rect x="1" y="38" width="16" height="40" fill="#eee"/><path d="M5 66h8M5 68h8" stroke="#bbb"/><path d="M4 141l5 6 5-6z" fill="var(--orange)"/></svg>
    </div>
  </div>

  <div class="abs month"><span class="caret-left"></span>February 2014<span class="caret-right"></span></div>
  <table class="abs cal">
    <tr><th>SUN</th><th>MON</th><th>TUE</th><th>WED</th><th>THU</th><th>FRI</th><th>SAT</th></tr>
    <tr><td></td><td>1</td><td>2</td><td>3</td><td>4</td><td>5</td><td>6</td></tr>
    <tr><td>7</td><td>8</td><td>9</td><td>10</td><td>11</td><td class="today">12</td><td>13</td></tr>
    <tr><td>14</td><td>15</td><td>16</td><td>17</td><td>18</td><td>19</td><td>20</td></tr>
    <tr><td>21</td><td>22</td><td>23</td><td>24</td><td>25</td><td>26</td><td>27</td></tr>
    <tr><td>28</td><td>29</td><td>30</td><td>31</td><td></td><td></td><td></td></tr>
  </table>
  <div class="abs download">
    <svg width="16" height="16" viewBox="0 0 16 16"><rect x="1" y="1" width="14" height="14" fill="none" stroke="var(--green)"/><path d="M1 5.5h14M1 10h14M5.5 1v14M10 1v14" stroke="var(--green)"/></svg>
    Download
  </div>

  <!-- footer -->
  <div class="abs footer-rule"></div>
  <div class="abs col-shadow" style="left:388px"></div>
  <div class="abs col-shadow" style="left:727px"></div>

  <div class="abs avatar" style="left:174px;background:radial-gradient(circle at 50% 70%,#ddd,#444 70%,#111)" role="img" aria-label="Black and white photo of a cup of coffee with beans"></div>
  <h3 class="abs col-title" style="left:113px">Helpful Info</h3>
  <ul class="abs links" style="left:155px">
    <li><span class="caret-down"></span>About us</li>
    <li>Media Enquiries</li>
    <li>Terms &amp; Conditions</li>
    <li>Privacy Policy</li>
  </ul>

  <div class="abs avatar" style="left:505px;background:radial-gradient(circle at 50% 45%,#bbb,#555 60%,#222)" role="img" aria-label="Black and white portrait of a team member"></div>
  <h3 class="abs col-title" style="left:443px">Who We Are</h3>
  <ul class="abs links" style="left:485px">
    <li><span class="caret-down"></span>How It Works</li>
    <li>FAQ</li>
    <li>Contact Us</li>
  </ul>

  <div class="abs avatar" style="left:844px;background:radial-gradient(circle at 50% 75%,#fff,#aaa 55%,#222)" role="img" aria-label="Black and white photo of a coffee cup filled with beans"></div>
  <h3 class="abs col-title" style="left:782px">Join Us On</h3>
  <ul class="abs social">
    <li><span class="icon"></span>Friendly</li>
    <li><span class="icon"></span>Chirper</li>
    <li><span class="icon"></span>Linkwork</li>
    <li><span class="icon"></span>Tubecast</li>
  </ul>

  <div class="abs bottom-band"></div>
  <p class="abs copyright">Copyright © 2014 Brewhaven</p>

</div>
</body>
</html>
```